we need a business card design for a professional painting business. This company has been up and going for about ten years. However it needs an new logo. we want this business card to be modern eye catching and easy to read. I currently have been looking for VP logos but can not find one that suits our needs. This Design should be Our start to a new beginning.
Industry/Entity Type
Painting
Contact Information for Business Card
Varesko Painting Inc.
Licensed & Insured
Tomas Varesko
Phone(631)384-4562
Fax (555) 846-3021
E-mail vareskopaintinginc@mailorbit.test
Requirements
Must have
- a new logo with  VP and i would like it to be in black and white.
i would also like the front to be a solid black with the logo only and then the back to have the information.

```html
<!DOCTYPE html>
<html lang="en">
<head>
<meta charset="utf-8">
<title>Varesko Painting Inc. – Business Card</title>
<link rel="stylesheet" href="https://fonts.googleapis.com/css2?family=Fondamento&family=Cormorant+Garamond:wght@500&display=swap">
<style>
  :root {
    --ink: #000000;
    --paper: #ffffff;
    --card-edge: #9a9a9a;
    --pattern-light: #ececec;
    --pattern-dark: #bdbdbd;
  }
  html, body {
    margin: 0;
    padding: 0;
    width: 1042px;
    height: 1200px;
    overflow: hidden;
    background: var(--paper);
  }
  .canvas {
    position: relative;
    width: 1042px;
    height: 1200px;
    background: var(--paper);
  }
  .card-front {
    position: absolute;
    left: 3px;
    top: 3px;
    width: 1036px;
    height: 574px;
    background: var(--ink);
  }
  .front-wordmark {
    position: absolute;
    left: 0;
    right: 0;
    top: 190px;
    text-align: center;
    font-family: "Fondamento", serif;
    font-size: 190px;
    line-height: 1;
    color: var(--paper);
  }
  .card-back {
    position: absolute;
    left: 2px;
    top: 621px;
    width: 1036px;
    height: 576px;
    background: var(--paper);
    border: 1px solid var(--card-edge);
  }
  .back-pattern-area {
    position: absolute;
    left: 384px;
    top: 14px;
    width: 292px;
    height: 466px;
    background: linear-gradient(to bottom, var(--pattern-dark), var(--pattern-light));
  }
  .contact-line {
    position: absolute;
    left: 0;
    right: 0;
    text-align: center;
    font-family: "Fondamento", serif;
    color: var(--ink);
    white-space: nowrap;
    line-height: 1;
    -webkit-text-stroke: 0.6px var(--ink);
  }
  .company-name { top: 280px; font-size: 46px; margin-left: -40px; }
  .license-owner { top: 348px; font-size: 43px; }
  .phone { top: 418px; font-size: 40px; margin-left: 30px; }
  .fax { top: 478px; font-size: 40px; margin-left: 26px; }
  .email {
    top: 530px;
    font-family: "Cormorant Garamond", serif;
    font-weight: 500;
    font-size: 38px;
    -webkit-text-stroke: 0;
    margin-left: 24px;
  }
</style>
</head>
<body>
<div class="canvas">
  <section class="card-front">
    <div class="front-wordmark">VP</div>
  </section>

  <section class="card-back">
    <div class="back-pattern-area" role="img" aria-label="Decorative paint-spray grid of fading black squares"></div>
    <div class="contact-line company-name">Varesko Painting Inc.</div>
    <div class="contact-line license-owner">Licensed &amp; Insured Tomas Varesko</div>
    <div class="contact-line phone">Phone(555)217-9083</div>
    <div class="contact-line fax">Fax (555) 846-3021</div>
    <div class="contact-line email">E-mail vareskopaintinginc@mailorbit.test</div>
  </section>
</div>
</body>
</html>
```